Psychotherapy and emotion coaching with feloQuin requires web design

I need a web design for emotion coaching (release of emotional blockages) (psychotherapy) with the target group trauma-related disorders and anxiety disorders. The website should be clear and well-organized, i.e. rather simple. The colors should be light, blue, green and yellow are desirable. The design should radiate security.

A logo already exists and should be used appropriately.

Three columns should describe the following
-Emotion regulation
-Imaginative structure constellations
-Ego-State-Therapy

An outdated draft can be seen here:
www.klarer-mutweg.example
The website should advertise coded in Wordpress.

I need the landing page, for which there are drafts now, and at least one more page (maybe a template) for further information (like "About me")

Target Market(s)

Clients for coaching and therapy with trauma or axienty disorders;

Coding

Coded - Design and coding required

Number of Pages Required

3 page

Font styles to use
Sans Serif

Colors
0054AA
0677BA
7BADD7
CADEEF
E8F1F8
59FF00
82FF00
B8FF75
E3FFCB
F4FFEA
FFF300
FFF600
FEFA6F
FFFEC7
FFFEE8

Requirements
Nice to have
• Title: "More happiness and satisfaction in life"
Should not have
• "Therapy" should not be listed in the header; Instead "More happiness and satisfaction in life"

```html
<!DOCTYPE html>
<html lang="de">
<head>
<meta charset="utf-8">
<title>Klarer Mutweg – Mehr Glück und Zufriedenheit im Leben</title>
<link href="https://fonts.googleapis.com/css2?family=Plus+Jakarta+Sans:wght@400;500;600;700;800&display=swap" rel="stylesheet">
<style>
:root{
  --blue:#0b4fa6;
  --blue-dark:#163b7a;
  --navy:#2b3b68;
  --yellow:#f3c42e;
  --orange:#f1a51b;
  --ink:#1f2328;
  --muted:#5b6068;
  --grey-bg:#f3f3f4;
  --white:#ffffff;
}
*{box-sizing:border-box;margin:0;padding:0}
html,body{width:1200px;height:4511px;overflow:hidden}
body{font-family:"Plus Jakarta Sans",sans-serif;color:var(--ink);background:var(--white);position:relative}
.abs{position:absolute}
a{color:inherit;text-decoration:none}

/* header */
.hero{left:0;top:0;width:1200px;height:690px;background:linear-gradient(180deg,#8fc3e6 0%,#b9d7e6 22%,#f0d9a0 42%,#e8a53b 55%,#a3581a 68%,#4a2a12 84%,#2a1a0e 100%)}
.topbar{left:0;top:0;width:1200px;height:90px;border-bottom:1px solid rgba(255,255,255,.45)}
.nav{left:138px;top:36px;display:flex;gap:46px;font-size:14px;font-weight:500}
.brand{left:484px;top:22px;display:flex;align-items:center;gap:14px}
.brand-mark{width:44px;height:44px;border-radius:50%;background:var(--yellow)}
.brand-name{font-size:16px;line-height:19px;color:#2b3b5c;font-weight:400}
.social{left:825px;top:30px;display:flex;align-items:center;gap:8px;font-size:14px;font-weight:500}
.social .label{margin-right:6px}
.hex{width:26px;height:28px;clip-path:polygon(50% 0,100% 25%,100% 75%,50% 100%,0 75%,0 25%);background:#2b2b2b}
.hex.y{background:var(--yellow)}
.hero-title{left:0;top:138px;width:1200px;text-align:center;font-size:54px;line-height:58px;font-weight:700;letter-spacing:-.5px}
.hero-sub{left:0;top:276px;width:1200px;text-align:center;font-size:18px;color:#2f2f2f}
.btn{display:inline-flex;align-items:center;justify-content:center;border-radius:5px;font-size:14px;font-weight:700}
.btn-blue{background:var(--blue);color:var(--white)}
.btn-yellow{background:var(--yellow);color:var(--ink)}
.hero-btn{left:430px;top:318px;width:340px;height:59px}
.arrow{width:42px;height:42px;border-radius:50%;background:rgba(40,50,70,.45);display:flex;align-items:center;justify-content:center}
.hero-shape{left:0;top:540px}

/* intro */
.intro-img{left:138px;top:733px;width:394px;height:513px;border-radius:4px;background:radial-gradient(circle at 50% 45%,#e8b64a 0%,#c48a2a 45%,#4a3a2a 100%)}
.intro-title{left:587px;top:778px;width:470px;font-size:29px;line-height:39px;font-weight:600}
.intro-text{left:587px;top:912px;width:460px;font-size:13.5px;line-height:23px;color:var(--muted)}
.intro-label{left:587px;top:1023px;font-size:14px;color:var(--blue);font-weight:500}
.check{display:flex;align-items:center;gap:10px;font-size:13px;font-weight:600}
.tick{width:16px;height:16px;border-radius:50%;background:#2a2a2a;display:flex;align-items:center;justify-content:center}
.intro-btn{left:590px;top:1146px;width:325px;height:57px}

/* services */
.services{left:0;top:1331px;width:1200px;height:981px;background:var(--grey-bg)}
.section-title{width:1200px;left:0;text-align:center;font-size:29px;font-weight:500}
.service{width:300px;text-align:center}
.service h3{font-size:16px;line-height:20px;font-weight:500;height:42px;display:flex;align-items:center;justify-content:center}
.service p{font-size:12.5px;line-height:23px;color:var(--muted);margin-top:10px}
.service .small{font-size:11.5px;line-height:23px}
.more{display:inline-flex;align-items:center;gap:4px;color:var(--blue);font-size:13px;font-weight:600;margin-top:14px}

/* coach card */
.coach{left:138px;top:2180px;width:910px;height:350px;border-radius:30px;background:linear-gradient(100deg,#0b4aa2 0%,#0f3f8f 55%,#15356f 100%);overflow:hidden}
.coach-photo{left:700px;top:2129px;width:320px;height:401px;border-radius:160px 160px 0 0;background:linear-gradient(180deg,#e8e2da 0%,#c9b9aa 40%,#3a6fd0 70%,#2456b8 100%);opacity:.92}
.coach-name{left:197px;top:2224px;font-size:38px;font-weight:800;color:var(--yellow)}
.coach-role{left:197px;top:2284px;width:400px;font-size:14px;line-height:23px;font-weight:700;color:var(--white)}
.coach-text{left:197px;top:2340px;width:460px;font-size:14px;line-height:23px;color:#e6ecf8}
.coach-btn1{left:197px;top:2428px;width:136px;height:56px}
.btn-outline{border:1.5px solid var(--white);color:var(--white)}
.coach-btn2{left:346px;top:2428px;width:112px;height:56px}

/* cta */
.cta-title{left:0;top:2612px;width:1200px;text-align:center;font-size:38px;font-weight:500}
.cta-text{left:250px;top:2686px;width:700px;text-align:center;font-size:16px;line-height:24px;color:var(--muted)}
.cta-btn{left:453px;top:2760px;width:324px;height:57px}

/* reviews */
.reviews{left:0;top:2894px;width:1200px;height:631px;background:var(--grey-bg)}
.card{background:var(--white);border-radius:14px}
.card.side{width:258px;height:270px;box-shadow:0 6px 20px rgba(0,0,0,.05)}
.card.main{width:354px;height:332px;box-shadow:0 10px 30px rgba(0,0,0,.1)}
.qhex{width:42px;height:46px;clip-path:polygon(50% 0,100% 25%,100% 75%,50% 100%,0 75%,0 25%);background:var(--blue);display:flex;align-items:center;justify-content:center}
.qhex i{width:38px;height:42px;clip-path:inherit;background:var(--white);display:flex;align-items:center;justify-content:center;font-style:normal;font-weight:800;color:var(--ink);font-size:16px}
.quote{font-size:10.5px;line-height:19px;color:var(--muted)}
.main .quote{font-size:13.5px;line-height:23px}
.rule{width:60px;height:1px;background:#999;margin:18px 0 12px}
.reviewer{font-size:11px;font-weight:600;color:var(--blue)}
.main .reviewer{font-size:13.5px}
.dots{left:568px;top:3428px;display:flex;gap:6px}
.dot{width:18px;height:20px;clip-path:polygon(50% 0,100% 25%,100% 75%,50% 100%,0 75%,0 25%);background:#555;display:flex;align-items:center;justify-content:center}
.dot i{width:16px;height:18px;clip-path:inherit;background:var(--grey-bg)}
.dot.on i{background:#333}

/* contact */
.contact-title{left:138px;top:3610px;font-size:34px;font-weight:500}
.contact-sub{left:138px;top:3690px;font-size:15px;font-weight:600}
.contact-text{left:138px;top:3726px;width:330px;font-size:13.5px;line-height:23px;color:var(--muted)}
.info{left:138px;display:flex;align-items:center;gap:20px}
.info-icon{width:54px;height:60px;clip-path:polygon(50% 0,100% 25%,100% 75%,50% 100%,0 75%,0 25%);background:#f6df90;display:flex;align-items:center;justify-content:center}
.info-label{font-size:13.5px;color:#333}
.info-value{font-size:13px;font-weight:600;margin-top:4px}
.info-value.link{color:var(--blue);font-weight:500;font-size:11.5px}
.form{left:589px;top:3612px;width:466px;height:488px;background:var(--blue);border-radius:10px;color:var(--white)}
.field-label{font-size:13.5px}
.input{background:var(--white);border-radius:2px;font-size:10.5px;color:#9a9ea6;padding:0 18px;display:flex;align-items:center}
.submit{left:624px;top:3999px;width:145px;height:48px;font-size:12px}
.thanks{left:700px;top:4160px;width:355px;text-align:right;font-size:13px;color:#444}

/* footer */
.footer{left:0;top:4160px;width:1200px;height:351px}
.foot-brand{left:150px;top:4290px;display:flex;align-items:center;gap:24px;color:var(--white)}
.foot-mark{width:62px;height:62px;border-radius:50%;background:var(--yellow)}
.foot-brand-name{font-size:23px;line-height:26px}
.foot-brand-name span{color:var(--yellow)}
.foot-text{left:537px;top:4297px;width:540px;font-size:14px;line-height:25px;color:#e9ecf5}
.foot-nav{left:146px;top:4395px;display:flex;gap:64px;color:var(--white);font-size:16px}
.foot-social{left:537px;top:4388px;display:flex;align-items:center;gap:14px;color:var(--white);font-size:16px}
.foot-social .hex{width:32px;height:36px;background:#5a5e6a}
.foot-social .hex.y{background:var(--yellow)}
.copy{left:0;top:4460px;width:1200px;height:51px;background:var(--yellow);display:flex;align-items:center;justify-content:center;font-size:12px;color:#333}
</style>
</head>
<body>

<!-- HERO -->
<section class="abs hero" role="img" aria-label="Foto einer Hügellandschaft im warmen Licht des Sonnenaufgangs"></section>
<svg class="abs hero-shape" width="1200" height="150" viewBox="0 0 1200 150" aria-hidden="true">
  <polygon points="0,30 960,140 1200,60 1200,150 0,150" fill="#f3b51c"/>
  <polygon points="0,20 960,122 1200,50 1200,150 0,150" fill="#ffffff"/>
</svg>
<header class="abs topbar">
  <nav class="abs nav"><a href="#">Startseite</a><a href="#">Über mich</a><a href="#">Kontakt</a></nav>
  <div class="abs brand"><span class="brand-mark"></span><span class="brand-name">Klarer Mutweg<br>…zur Gelassenheit</span></div>
  <div class="abs social"><span class="label">Folge Uns Auf</span><span class="hex"></span><span class="hex y"></span><span class="hex"></span><span class="hex"></span></div>
</header>
<h1 class="abs hero-title">Mehr Glück Und<br>Zufriedenheit Im Leben</h1>
<p class="abs hero-sub">Befreiung Von Emotionalen Blockaden</p>
<a class="abs btn btn-blue hero-btn" href="#">Kostenloses Erstgespräch Vereinbaren</a>
<span class="abs arrow" style="left:138px;top:239px"><svg width="10" height="10" viewBox="0 0 10 10"><path d="M6.5 1.5 3 5l3.5 3.5" stroke="#fff" stroke-width="1.4" fill="none"/></svg></span>
<span class="abs arrow" style="left:1015px;top:239px"><svg width="10" height="10" viewBox="0 0 10 10"><path d="M3.5 1.5 7 5 3.5 8.5" stroke="#fff" stroke-width="1.4" fill="none"/></svg></span>

<!-- INTRO -->
<div class="abs intro-img" role="img" aria-label="Illustration einer Frau mit geschlossenen Augen vor goldenem Hintergrund"></div>
<h2 class="abs intro-title">Leidest du unter Angstzuständen, Traumata oder emotionalen Belastungen?</h2>
<p class="abs intro-text">Unser Gehirn merkt sich Erfahrungen, die schwerwiegend waren oder uns in einer traumatischen Situation überfordert haben. Wenn wir unbewusst an solche Erfahrungen erinnert werden, sind wir nicht mehr voll und ganz handlungsfähig und fühlen uns schlecht</p>
<p class="abs intro-label">Vorteile</p>
<div class="abs check" style="left:587px;top:1060px"><span class="tick"><svg width="9" height="9" viewBox="0 0 10 10"><path d="M2 5.2 4.2 7.4 8 2.8" stroke="#fff" stroke-width="1.6" fill="none"/></svg></span>Verbesserte Emotionsregulierung</div>
<div class="abs check" style="left:587px;top:1097px"><span class="tick"><svg width="9" height="9" viewBox="0 0 10 10"><path d="M2 5.2 4.2 7.4 8 2.8" stroke="#fff" stroke-width="1.6" fill="none"/></svg></span>Größeres Selbstbewusstsein</div>
<div class="abs check" style="left:858px;top:1088px"><span class="tick"><svg width="9" height="9" viewBox="0 0 10 10"><path d="M2 5.2 4.2 7.4 8 2.8" stroke="#fff" stroke-width="1.6" fill="none"/></svg></span>Geringere Ängste</div>
<a class="abs btn btn-blue intro-btn" href="#">Kostenloses Erstgespräch Vereinbaren</a>

<!-- SERVICES -->
<section class="abs services"></section>
<h2 class="abs section-title" style="top:1408px">Unsere Dienstleistungen</h2>
<svg class="abs" style="left:164px;top:1487px" width="246" height="268" viewBox="0 0 246 268" role="img" aria-label="Foto eines Mannes, der nachdenklich auf einem Stuhl sitzt">
  <polygon points="123,4 242,69 242,199 123,264 4,199 4,69" fill="#8c8278" stroke="#0b4fa6" stroke-width="3"/>
</svg>
<svg class="abs" style="left:477px;top:1487px" width="246" height="268" viewBox="0 0 246 268" role="img" aria-label="Foto einer lachenden Frau im Gras">
  <polygon points="123,4 242,69 242,199 123,264 4,199 4,69" fill="#6f8f4e" stroke="#f3c42e" stroke-width="3"/>
</svg>
<svg class="abs" style="left:790px;top:1487px" width="246" height="268" viewBox="0 0 246 268" role="img" aria-label="Foto zweier Personen in einer Therapiesitzung">
  <polygon points="123,4 242,69 242,199 123,264 4,199 4,69" fill="#d9d6d2" stroke="#0b4fa6" stroke-width="3"/>
</svg>
<div class="abs service" style="left:136px;top:1770px">
  <h3>Regulierung von<br>Emotionen</h3>
  <p class="small">Mittels dieser Technik werden gezielt die im Gehirn gespeicherten Erfahrungen, die uns blockieren, positiv verändert. In der Folge gewinnst Du an Selbstvertrauen und Selbstwirksamkeit.</p>
  <a class="more" href="#">Mehr lesen <svg width="10" height="10" viewBox="0 0 10 10"><path d="M2 3.5 5 6.5 8 3.5" stroke="#0b4fa6" stroke-width="1.5" fill="none"/></svg></a>
</div>
<div class="abs service" style="left:450px;top:1770px">
  <h3>Systemische<br>Strukturaufstellungen</h3>
  <p>Wir alle haben überkommene Prägungen und Muster, die immer wieder Konflikte verursachen oder uns ausbremsen. In einer Aufstellung werden alte Muster aufgedeckt und verändert, sodass du an Klarheit und Selbstakzeptanz gewinnst und es dir mehr und mehr gelingt, eine glückliche Partnerschaft zu führen oder sich Konflikte im Team lösen.</p>
  <a class="more" href="#">Ausblenden <svg width="10" height="10" viewBox="0 0 10 10"><path d="M2 6.5 5 3.5 8 6.5" stroke="#0b4fa6" stroke-width="1.5" fill="none"/></svg></a>
</div>
<div class="abs service" style="left:762px;top:1770px">
  <h3>Ego-State-Therapie</h3>
  <p class="small">Mittels dieser Technik werden gezielt die im Gehirn gespeicherten Erfahrungen, die uns blockieren, positiv verändert. In der Folge gewinnst Du an Selbstvertrauen und Selbstwirksamkeit.</p>
  <a class="more" href="#">Mehr lesen <svg width="10" height="10" viewBox="0 0 10 10"><path d="M2 3.5 5 6.5 8 3.5" stroke="#0b4fa6" stroke-width="1.5" fill="none"/></svg></a>
</div>

<!-- COACH -->
<section class="abs coach"></section>
<div class="abs coach-photo" role="img" aria-label="Porträtfoto des Beraters Jonas Lindner im blauen Pullover"></div>
<h2 class="abs coach-name">Jonas Lindner</h2>
<p class="abs coach-role">Psychotherapie, Psychoonkologie oder Coaching mit feloQuin® oder EMDR</p>
<p class="abs coach-text">Die Themen Heilung, persönliches Wachstum, Ganzwerdung und Selbsterkenntnis begleiten mich schon mein ganzes Leben. Ich bin seit November 2021 zertifizierter feloQuin® Coach</p>
<a class="abs btn btn-yellow coach-btn1" href="#">Mehr Lesen</a>
<a class="abs btn btn-outline coach-btn2" href="#">Kontakt</a>

<!-- CTA -->
<h2 class="abs cta-title">Bereit, Den Ersten Schritt Zu Gehen?</h2>
<p class="abs cta-text">Ermutigen Sie potenzielle Kunden, ein kostenloses Beratungsgespräch zu vereinbaren, um ihre Ziele und die Möglichkeiten Ihrer Dienstleistungen zu besprechen.</p>
<a class="abs btn btn-yellow cta-btn" href="#">Kostenloses Erstgespräch Vereinbaren</a>

<!-- REVIEWS -->
<section class="abs reviews"></section>
<h2 class="abs section-title" style="top:2982px">Kundenrezensionen</h2>
<div class="abs card side" style="left:183px;top:3087px;padding:32px 24px;overflow:hidden">
  <div class="qhex" style="margin:0 0 20px 95px;width:42px;height:46px"><i>“</i></div>
  <p class="quote" style="width:250px">Lorem ipsum dolor sit amet consectetur. Facilisi a tellus consequat nunc maecenas ante lectus. Facilisi egestas adipiscing feugiat non. Non curabitur vulputate dignissim ac purus ipsum volutpat faucibus.</p>
  <div class="rule"></div><p class="reviewer">Maren Olsen</p>
</div>
<div class="abs card side" style="left:758px;top:3087px;padding:32px 24px;overflow:hidden">
  <div class="qhex" style="margin:0 0 20px 85px"><i>“</i></div>
  <p class="quote" style="margin-left:-20px">m ipsum dolor sit amet consectetur. si a tellus consequat nunc maecenas ante s. Facilisi egestas adipiscing feugiat non. curabitur vulputate dignissim ac purus n volutpat faucibus.</p>
  <div class="rule" style="margin-left:-20px;width:30px"></div><p class="reviewer" style="margin-left:-20px">ie Olsen</p>
</div>
<div class="abs card main" style="left:423px;top:3057px;padding:38px 30px">
  <div class="qhex" style="margin:0 0 22px 132px;width:48px;height:54px"><i style="width:44px;height:50px">“</i></div>
  <p class="quote">Lorem ipsum dolor sit amet consectetur. Facilisi a tellus consequat nunc maecenas ante lectus. Facilisi egestas adipiscing feugiat non. Non curabitur vulputate dignissim ac purus ipsum volutpat faucibus.</p>
  <div class="rule" style="width:72px"></div><p class="reviewer">Maren Olsen</p>
</div>
<div class="abs dots"><span class="dot"><i></i></span><span class="dot on"><i></i></span><span class="dot"><i></i></span></div>

<!-- CONTACT -->
<h2 class="abs contact-title">Kontakt Mit Uns</h2>
<p class="abs contact-sub">Ihr Berater Jonas</p>
<p class="abs contact-text">Wenn Sie Interesse an meinem Angebot oder Fragen dazu haben, rufen Sie mich gerne an oder schreiben mir eine E-Mail.</p>
<div class="abs info" style="top:3806px"><span class="info-icon"><svg width="24" height="24" viewBox="0 0 24 24"><circle cx="10" cy="8" r="4" fill="#222"/><path d="M3 20c0-4 3-6 7-6s7 2 7 6z" fill="#222"/></svg></span><div><p class="info-label" style="font-weight:600">Jonas Lindner</p><p class="info-value link">Heilpraktiker für Psychotherapie</p></div></div>
<div class="abs info" style="top:3884px"><span class="info-icon"><svg width="22" height="24" viewBox="0 0 22 24"><path d="M11 2a7 7 0 0 0-7 7c0 5 7 13 7 13s7-8 7-13a7 7 0 0 0-7-7z" fill="#222"/><circle cx="11" cy="9" r="2.6" fill="#f6df90"/></svg></span><div><p class="info-label">Adresse</p><p class="info-value">Birkenallee 12, 30159 Musterstadt</p></div></div>
<div class="abs info" style="top:3967px"><span class="info-icon"><svg width="24" height="18" viewBox="0 0 24 18"><rect x="1" y="1" width="22" height="16" rx="2" fill="none" stroke="#222" stroke-width="2"/><path d="M2 2l10 8 10-8" fill="none" stroke="#222" stroke-width="2"/></svg></span><div><p class="info-label">E-mail</p><p class="info-value">kontakt@klarer-mutweg.example</p></div></div>
<div class="abs info" style="top:4051px"><span class="info-icon"><svg width="22" height="22" viewBox="0 0 24 24"><path d="M6.6 10.8a15 15 0 0 0 6.6 6.6l2.2-2.2a1 1 0 0 1 1-.25 11.4 11.4 0 0 0 3.6.57 1 1 0 0 1 1 1V20a1 1 0 0 1-1 1A17 17 0 0 1 3 4a1 1 0 0 1 1-1h3.5a1 1 0 0 1 1 1c0 1.25.2 2.45.57 3.6a1 1 0 0 1-.25 1z" fill="#222"/></svg></span><div><p class="info-label">Telefonnummer</p><p class="info-value">0170 000 48 215</p></div></div>

<form class="abs form">
  <label class="abs field-label" style="left:35px;top:52px">Vorname</label>
  <label class="abs field-label" style="left:244px;top:52px">Nachname</label>
  <div class="abs input" style="left:35px;top:84px;width:188px;height:40px">Hier tippen</div>
  <div class="abs input" style="left:244px;top:84px;width:188px;height:40px">Hier tippen</div>
  <label class="abs field-label" style="left:35px;top:150px">Rufnummer</label>
  <label class="abs field-label" style="left:244px;top:150px">E-Mail Adresse</label>
  <div class="abs input" style="left:35px;top:181px;width:188px;height:40px">Hier tippen</div>
  <div class="abs input" style="left:244px;top:181px;width:188px;height:40px">Hier tippen</div>
  <label class="abs field-label" style="left:35px;top:253px">Ihre Nachricht</label>
  <div class="abs input" style="left:35px;top:284px;width:397px;height:84px;align-items:flex-start;padding-top:14px">Geben Sie Ihre Nachricht ein</div>
</form>
<a class="abs btn btn-yellow submit" href="#">Einreichen</a>
<p class="abs thanks">Ich freue mich uns über Ihre Kontaktaufnahme!</p>

<!-- FOOTER -->
<svg class="abs footer" width="1200" height="300" viewBox="0 0 1200 300" aria-hidden="true">
  <defs><linearGradient id="footBg" x1="0" y1="0" x2="0" y2="1"><stop offset="0" stop-color="#3a4a78"/><stop offset="1" stop-color="#25345e"/></linearGradient></defs>
  <polygon points="0,70 260,20 1200,55 1200,300 0,300" fill="#f1a51b"/>
  <polygon points="0,88 260,40 1200,72 1200,300 0,300" fill="url(#footBg)"/>
</svg>
<div class="abs foot-brand"><span class="foot-mark"></span><span class="foot-brand-name">Klarer Mutweg<br><span>…zur Gelassenheit</span></span></div>
<p class="abs foot-text">Unser Gehirn merkt sich Erfahrungen, die schwerwiegend waren oder uns in einer traumatischen Situation überfordert haben.</p>
<nav class="abs foot-nav"><a href="#">Startseite</a><a href="#">Über mich</a><a href="#">Kontakt</a></nav>
<div class="abs foot-social"><span>Folge Uns Auf</span><span class="hex"></span><span class="hex y"></span><span class="hex"></span><span class="hex"></span></div>
<footer class="abs copy">Urheberrecht 2024. Klarer Mutweg, zur Gelassenheit. Alle Rechte vorbehalten.</footer>

</body>
</html>
```